Company Values Graphic

We are looking for a design of our company values that can be used in a variety of places including our website, mousepads, office posters, business cards, etc.

Notes:
- We'd rather have icons/art than photographs on the poster.... so more like an infographic
- The core value group headings are not required, but can be included if you think grouping the values works for your design
- We have a logo for our software product but that logo is not required
- We don't need/want clever images to accompany each value, but some images are fine
- BrightNest logo attached
- BrightNest colors are attached
- BrightNest logo is Nunito Sans ExtraBold 800
- BrightNest website uses Roboto

Our Values - Who we will work with (and who we will not)
The right set of values are essential to building and maintaining a culture that we all wake up eager to be a part of each day. They are foundational to all hiring and firing decisions. They attract the right people and repel the wrong ones.

BE HELPFUL
Make every person and place better because you are there.
Deliver wow with every interaction.

BE HUMBLE
Listen with every muscle.
Passionately help others first.
Seek first to understand.

BE HONEST
Earn trust every day.
Be open and direct.
Treat everyone with fairness and respect.

BE HUMAN
Celebrate passion and action.
Create an environment where people are authentic.
Hire great people and expect a lot from them

BE COURAGEOUS
Dare mighty things.
Make and honor commitments.
All great things start with a small act of courage applied at the right moment.

```html
<!DOCTYPE html>
<html lang="en">
<head>
<meta charset="utf-8">
<title>BrightNest — Our Values</title>
<link href="https://fonts.googleapis.com/css2?family=Montserrat:wght@400;800&display=swap" rel="stylesheet">
<style>
  :root {
    --brand-orange: #f15a24;
    --brand-red: #ec2227;
    --brand-amber: #f7991e;
    --ink: #111111;
    --body-ink: #2a2a2a;
    --paper: #ffffff;
  }
  html, body { margin: 0; padding: 0; overflow: hidden; background: var(--paper); }
  .canvas {
    position: relative; width: 1200px; height: 1000px; overflow: hidden;
    background: var(--paper); font-family: "Montserrat", Arial, sans-serif; color: var(--body-ink);
  }
  .brand {
    position: absolute; left: 662px; top: 68px; display: flex; align-items: center; gap: 26px;
  }
  .brand-dot { width: 100px; height: 100px; border-radius: 50%; background: var(--brand-orange); }
  .brand-name {
    font-weight: 800; font-size: 66px; color: var(--ink); letter-spacing: -0.5px; line-height: 1;
  }
  .side-title {
    position: absolute; left: 170px; top: 542px; transform: translate(-50%, -50%) rotate(-90deg);
    font-weight: 800; font-size: 22px; letter-spacing: 31px; white-space: nowrap; color: var(--ink);
  }
  .card {
    position: absolute; left: 207px; top: 263px; width: 849px; height: 560px; box-sizing: border-box;
    border: 13px solid var(--brand-orange); border-left: none; border-radius: 0 36px 36px 0;
    box-shadow: -6px 4px 10px rgba(0,0,0,0.25);
  }
  .intro { position: absolute; left: 270px; top: 351px; width: 262px; text-align: right; }
  .intro-heading {
    margin: 0; font-weight: 800; font-size: 17.5px; line-height: 16px; color: var(--brand-orange);
  }
  .intro-text { margin: 19px 0 0; font-size: 11.6px; line-height: 14.4px; }
  .mascot {
    position: absolute; left: 320px; top: 505px; width: 183px; height: 241px;
    background: linear-gradient(160deg, var(--brand-amber), var(--brand-orange) 55%, var(--brand-red));
    clip-path: polygon(0 15%, 68% 0, 100% 15%, 100% 100%, 0 100%);
  }
  .connectors { position: absolute; left: 0; top: 0; }
  .value { position: absolute; left: 680px; width: 340px; }
  .value-title {
    margin: 0; font-weight: 800; font-size: 17px; line-height: 18px; color: var(--brand-orange);
  }
  .value-text { margin: 1px 0 0; font-size: 11.6px; line-height: 14.4px; }
</style>
</head>
<body>
<div class="canvas">
  <div class="brand">
    <div class="brand-dot"></div>
    <div class="brand-name">BrightNest</div>
  </div>

  <div class="side-title">OUR VALUE</div>

  <div class="card"></div>

  <div class="intro">
    <h2 class="intro-heading">WHO WE WILL WORK WITH<br>(AND WHO WE WILL NOT)</h2>
    <p class="intro-text">The right set of values are essential to building and maintaining a culture that we all wake up eager to be a part of each day. They are foundational to all hiring and firing decisions. They attract the right people and repel the wrong ones.</p>
  </div>

  <div class="mascot" role="img" aria-label="Illustration of a figure carrying a flame inside a house outline"></div>

  <svg class="connectors" width="1200" height="1000" viewBox="0 0 1200 1000" aria-hidden="true">
    <g fill="none" stroke="var(--brand-orange)" stroke-width="1">
      <polyline points="503,711 559,711 559,375"/>
      <line x1="559" y1="375" x2="617" y2="375"/>
      <line x1="559" y1="439" x2="617" y2="439"/>
      <line x1="559" y1="517" x2="617" y2="517"/>
      <line x1="559" y1="596" x2="617" y2="596"/>
      <line x1="559" y1="674" x2="617" y2="674"/>
    </g>
    <g class="ticks">
      <g transform="translate(638,375)"><circle r="21.5" fill="var(--brand-orange)"/><polyline points="-11,0 -3,8 11,-11" fill="none" stroke="#fff" stroke-width="2.5"/></g>
      <g transform="translate(638,439)"><circle r="21.5" fill="var(--brand-orange)"/><polyline points="-11,0 -3,8 11,-11" fill="none" stroke="#fff" stroke-width="2.5"/></g>
      <g transform="translate(638,517)"><circle r="21.5" fill="var(--brand-orange)"/><polyline points="-11,0 -3,8 11,-11" fill="none" stroke="#fff" stroke-width="2.5"/></g>
      <g transform="translate(638,596)"><circle r="21.5" fill="var(--brand-orange)"/><polyline points="-11,0 -3,8 11,-11" fill="none" stroke="#fff" stroke-width="2.5"/></g>
      <g transform="translate(638,674)"><circle r="21.5" fill="var(--brand-orange)"/><polyline points="-11,0 -3,8 11,-11" fill="none" stroke="#fff" stroke-width="2.5"/></g>
    </g>
  </svg>

  <div class="value" style="top:352px">
    <h3 class="value-title">BE HELPFUL</h3>
    <p class="value-text">Make every person and place better because you are there.<br>Deliver wow with every interaction.</p>
  </div>
  <div class="value" style="top:416px">
    <h3 class="value-title">BE HUMBLE</h3>
    <p class="value-text">Listen with every muscle.<br>Passionately help others first.<br>Seek first to understand.</p>
  </div>
  <div class="value" style="top:495px">
    <h3 class="value-title">BE HONEST</h3>
    <p class="value-text">Earn trust every day.<br>Be open and direct.<br>Treat everyone with fairness and respect.</p>
  </div>
  <div class="value" style="top:573px">
    <h3 class="value-title">BE HUMAN</h3>
    <p class="value-text">Celebrate passion and action.<br>Create an environment where people are authentic.<br>Hire great people and expect a lot from them</p>
  </div>
  <div class="value" style="top:652px">
    <h3 class="value-title">BE COURAGEOUS</h3>
    <p class="value-text">Dare mighty things.<br>Make and honor commitments.<br>All great things start with a small act of courage applied at the right moment.</p>
  </div>
</div>
</body>
</html>
```